New Dental Office Needs an Attractive and user friendly Website Designed

I need a website for a new dental office. The Name is Maplecrest Dentistry. I would like a Modern design with a user friendly interface and usability.
I would like a landing page, a page that lists the services we offer: Cosmetic Dentistry, Implants, Dental Hygiene, Emergency Services, Restorations, Dentures
Target Market(s)
Mid to upper class
Industry/Entity Type
Dentistry
Coding
Coded - Design and coding required
Number of Pages Required
1 page
Requirements
Must have
- Landing page that has a scheduling option, Procedures, operating hours, and contact us info
Nice to have
- Appealing design, Soft comforting colors. Easy to navigate page, Modern and professional.

```html
<!DOCTYPE html>
<html lang="en">
<head>
<meta charset="utf-8">
<title>Maplecrest Dentistry – Website Design</title>
<link href="https://fonts.googleapis.com/css2?family=Prata&family=Poppins:wght@400;500;600&family=Dancing+Script:wght@600&display=swap" rel="stylesheet">
<style>
:root{
  --board:#e4e4e4;
  --dark:#28241f;
  --dark-2:#2e2925;
  --gold:#f3a93a;
  --gold-text:#eaa52c;
  --white:#ffffff;
  --ink:#2a2a2a;
  --muted:#d9d4cc;
  --light:#f5f5f5;
}
*{margin:0;padding:0;box-sizing:border-box}
html,body{width:960px;height:1200px;overflow:hidden;background:var(--board)}
body{position:relative;font-family:'Poppins',sans-serif;color:var(--white)}
.abs{position:absolute}
.center{transform:translateX(-50%);white-space:nowrap;text-align:center}
.serif{font-family:'Prata',serif;font-weight:400}
.gold{color:var(--gold-text)}
.btn{position:absolute;background:var(--gold);border-radius:20px;color:var(--dark);font-size:3.6px;font-weight:500;display:flex;align-items:center;justify-content:center;gap:2px;white-space:nowrap}
.btn svg{width:4px;height:4px}

/* ---------- landing page ---------- */
.site{position:absolute;left:84.6px;top:36.7px;width:384px;height:1114.4px;overflow:hidden;background:var(--dark)}

.hero{position:absolute;left:0;top:0;width:384px;height:240px;
  background:radial-gradient(ellipse at 68% 28%,#b8826a 0%,#7a4a36 22%,#3a2519 50%,#1c1612 80%),#1c1612}
.nav a{position:absolute;top:15.8px;font-size:3.8px;color:var(--white);text-decoration:none;white-space:nowrap}
.brand{font-family:'Prata',serif;color:var(--white);white-space:nowrap}
.slider-arrow{position:absolute;width:11px;height:11px;border-radius:50%;border:0.6px solid rgba(255,255,255,.6);display:flex;align-items:center;justify-content:center}
.slider-arrow svg{width:4px;height:4px}
.dots{position:absolute;display:flex;gap:4.6px;transform:translateX(-50%)}
.dots span{width:1.8px;height:1.8px;border-radius:50%;background:#fff}
.dots span.on{background:var(--gold);box-shadow:0 0 0 .6px rgba(243,169,58,.5)}

.welcome .para{position:absolute;left:208.7px;width:110px;font-size:3.05px;line-height:5.25px;color:var(--muted)}
.rule{position:absolute;height:0.5px;background:var(--gold)}

.services{position:absolute;left:0;width:384px;height:300px;background:var(--white);color:var(--ink)}
.card{position:absolute;width:95.3px;height:90px;overflow:hidden}
.card .title{position:absolute;left:0;width:100%;text-align:center;font-family:'Prata',serif;font-size:5.4px;color:#fff}
.card .title::after{content:"";display:block;margin:1.4px auto 0;width:50px;height:0.4px;background:rgba(255,255,255,.6)}
.card .desc{position:absolute;left:8px;right:8px;text-align:center;font-size:3.4px;line-height:4.4px;color:#fff}

.why{position:absolute;left:0;top:756.8px;width:384px;height:156px;background:var(--dark)}
.why li{position:absolute;left:221px;list-style:none;font-size:3.7px;display:flex;align-items:center;gap:3px;white-space:nowrap}
.why li svg{width:3.8px;height:3.8px}

.reviews{position:absolute;left:0;top:912.7px;width:384px;height:202px;background:var(--light);color:var(--ink)}
.review{position:absolute;width:145.5px;height:96px;background:#fff;border:0.5px solid #ececec}
.review .inner{position:absolute;inset:2.6px;border:0.5px solid #e2e2e2}
.review .avatar{position:absolute;left:10px;top:22px;width:50px;height:50px;border-radius:50%}
.review .stars{position:absolute;left:68px;top:18px;font-size:4.4px;letter-spacing:0.6px;color:var(--gold)}
.review .text{position:absolute;left:68px;width:72px;top:32px;font-size:3.2px;line-height:5.4px;color:#444}
.review .who{position:absolute;left:68px;top:64px;display:flex;align-items:center;gap:2.4px}
.review .who i{width:4.4px;height:4.4px;border-radius:50%;background:#d5d5d5;display:block}
.review .name{font-family:'Prata',serif;font-size:3.8px;line-height:4px;color:#222}
.review .role{font-size:2.6px;color:#666}
.review .quote{position:absolute;left:117px;top:58px;font-family:'Prata',serif;font-size:28px;line-height:28px;color:#f0cc7a}

/* ---------- contact & footer ---------- */
.contact{position:absolute;left:513.6px;top:36.7px;width:384px;height:361px;background:var(--dark);overflow:hidden}
.team-photo{position:absolute;left:0;top:0;width:384px;height:189px;
  background:linear-gradient(100deg,#f2ece6 0%,#e9ddd1 35%,#efe4da 55%,#e7b889 80%,#dca070 100%)}
.form-box{position:absolute;left:202px;top:33.4px;width:149.7px;height:122.4px;background:var(--dark-2);border:0.5px solid rgba(243,169,58,.5)}
.field{position:absolute;border:0.5px solid rgba(243,169,58,.8);font-size:2.8px;color:var(--gold-text);padding:2.2px 3.4px;white-space:nowrap}
.footer-head{position:absolute;font-size:4.4px;color:#fff;white-space:nowrap}
.footer-links a{position:absolute;left:82.4px;font-size:3.5px;color:#e6e1da;text-decoration:none;white-space:nowrap}
.social{position:absolute;top:291px;width:12px;height:12px;border-radius:50%;border:0.6px solid var(--gold)}
.social::after{content:"";position:absolute;left:4px;top:4px;width:3px;height:3px;border-radius:50%;background:#fff}
.c-item{position:absolute;left:305.6px;width:72px;display:flex;gap:3.4px;font-size:3.2px;line-height:4.4px;color:#e6e1da}
.c-item svg{width:4.2px;height:4.2px;flex:none;margin-top:.2px}

.thanks{position:absolute;left:705.6px;top:480px;transform:translateX(-50%);font-family:'Dancing Script',cursive;font-size:40px;color:#222;white-space:nowrap}
</style>
</head>
<body>

<main class="site">
  <!-- Hero -->
  <section class="hero" role="img" aria-label="Close-up photo of a smiling woman with healthy white teeth and long dark hair"></section>
  <nav class="nav">
    <a style="left:37px">Home</a>
    <a style="left:60px">About</a>
    <a style="left:82px">Services</a>
    <a style="left:110px">Testimonials</a>
    <a style="left:241px">Blogs</a>
    <a style="left:264px">Contact</a>
  </nav>
  <div class="brand abs center" style="left:192px;top:13.5px;font-size:7px">Maplecrest Dentistry</div>
  <a class="btn" style="left:289px;top:11.7px;width:58px;height:12.8px">
    <svg viewBox="0 0 24 24"><path fill="#28241f" d="M6.6 10.8a15 15 0 0 0 6.6 6.6l2.2-2.2c.3-.3.7-.4 1-.2 1.1.4 2.3.6 3.6.6.6 0 1 .4 1 1V20c0 .6-.4 1-1 1A17 17 0 0 1 3 4c0-.6.4-1 1-1h3.5c.6 0 1 .4 1 1 0 1.3.2 2.5.6 3.6.1.3 0 .7-.2 1z"/></svg>Book Appointment</a>

  <div class="abs center gold" style="left:192px;top:110.5px;font-size:6.7px">Your Smile Starts Here</div>
  <h1 class="abs center serif" style="left:192px;top:121px;font-size:14.3px;line-height:17.4px">Modern Dental Care With Comfort,<br>Compassion, &amp; Confidence.</h1>
  <a class="btn" style="left:162.5px;top:164.7px;width:58.5px;height:12.8px">
    <svg viewBox="0 0 24 24"><path fill="#28241f" d="M6.6 10.8a15 15 0 0 0 6.6 6.6l2.2-2.2c.3-.3.7-.4 1-.2 1.1.4 2.3.6 3.6.6.6 0 1 .4 1 1V20c0 .6-.4 1-1 1A17 17 0 0 1 3 4c0-.6.4-1 1-1h3.5c.6 0 1 .4 1 1 0 1.3.2 2.5.6 3.6.1.3 0 .7-.2 1z"/></svg>Book Appointment</a>
  <div class="slider-arrow" style="left:24px;top:114px"><svg viewBox="0 0 24 24"><path d="M15 5l-7 7 7 7" stroke="#fff" stroke-width="2" fill="none"/></svg></div>
  <div class="slider-arrow" style="left:348.5px;top:114px;border-color:rgba(243,169,58,.6)"><svg viewBox="0 0 24 24"><path d="M9 5l7 7-7 7" stroke="#f3a93a" stroke-width="2" fill="none"/></svg></div>
  <div class="dots" style="left:192px;top:211px"><span></span><span></span><span class="on"></span><span></span><span></span></div>

  <!-- Welcome -->
  <section class="welcome">
    <div class="rule" style="left:116px;top:268.6px;width:30px"></div>
    <div class="rule" style="left:238px;top:268.6px;width:29px"></div>
    <div class="abs center gold" style="left:192px;top:264.6px;font-size:6.2px;line-height:8px">Welcome to Maplecrest</div>
    <h2 class="abs center serif" style="left:192px;top:273.5px;font-size:12.8px;line-height:14.2px">We Provide Best Dental<br>Services</h2>

    <div class="abs" style="left:63px;top:303.8px;width:50.5px;height:74px;border:0.6px solid var(--gold)"></div>
    <div class="abs" role="img" aria-label="Photo of a dentist treating a patient's teeth with a dental drill" style="left:66.8px;top:307.7px;width:99px;height:94.6px;border-top-right-radius:16px;background:linear-gradient(135deg,#e9c9bd 0%,#c99585 45%,#b9c7d8 80%,#8fb4de 100%)"></div>
    <div class="abs" role="img" aria-label="Photo of a smiling dentist with a female patient in the dental chair" style="left:125px;top:356px;width:75px;height:72px;border:2px solid #111;background:linear-gradient(120deg,#e7edf2 0%,#c9d6e2 45%,#9fb2c6 75%,#e3c7b6 100%)"></div>

    <p class="para" style="top:313.5px">Compassionate Dentistry With A Modern Touch Maplecrest Dentistry Was Founded On The Principles Of Personalized Care And Clinical Excellence. Our Highly Trained Team Blends The Latest In Dental Innovation With A Friendly, Welcoming Environment Designed To Put You At Ease. Whether You're Here For A Routine Visit Or Specialized Treatment, Our Focus Is Always Your Health, Comfort, And Satisfaction.</p>
    <p class="para" style="top:355.8px">Our Dentists Bring Years Of Experience Across General, Cosmetic, And Restorative Dentistry, And They Are Continuously Learning To Stay Ahead Of Advancements In Dental Science And Patient Care. At Maplecrest Dentistry, You're Not Just A Patient — You're Part Of Our Dental Family.</p>
    <a class="btn" style="left:208.7px;top:392.9px;width:64px;height:12.8px">Read More About Us
      <svg viewBox="0 0 24 24"><path d="M4 12h15M13 6l6 6-6 6" stroke="#28241f" stroke-width="2.4" fill="none"/></svg></a>
  </section>

  <!-- Services -->
  <section class="services" style="top:456.8px">
    <h2 class="abs center serif" style="left:192px;top:20px;font-size:13.2px">What Service Provide</h2>
    <div class="rule" style="left:152px;top:41.8px;width:20px"></div>
    <div class="rule" style="left:210.8px;top:41.8px;width:20px"></div>
    <div class="abs center gold" style="left:192px;top:39.2px;font-size:4.4px">Our Services</div>

    <article class="card" style="left:41.7px;top:55px" role="img" aria-label="Close-up photo of a bright white smile">
      <div class="abs" style="inset:0;background:linear-gradient(180deg,#e6d2cf 0%,#c98f8b 35%,#7c4d4c 60%,#2a1d1d 100%)"></div>
      <div class="title" style="top:62px">Cosmetic Dentistry</div>
      <div class="desc" style="top:72.5px">Brighten, straighten, and enhance your smile.</div>
    </article>
    <article class="card" style="left:144.6px;top:55px" role="img" aria-label="Rendering of a dental implant with crown">
      <div class="abs" style="inset:0;background:linear-gradient(180deg,#e8e8e8 0%,#6b6b6b 30%,#2a2420 48%,#8a6a2c 75%,#e0a93a 100%)"></div>
      <div class="title" style="top:35px">Dental Implants</div>
      <div class="desc" style="top:45.5px">Permanent solutions for missing teeth.</div>
    </article>
    <article class="card" style="left:246.8px;top:55px" role="img" aria-label="Photo of a woman brushing her teeth">
      <div class="abs" style="inset:0;background:linear-gradient(180deg,#e7d8d2 0%,#c7a69c 35%,#6e5552 62%,#1f1a1a 100%)"></div>
      <div class="title" style="top:62px">Dental Hygiene</div>
      <div class="desc" style="top:72.5px">Preventive care to keep your smile healthy.</div>
    </article>
    <article class="card" style="left:41.7px;top:151.8px" role="img" aria-label="Photo of a dentist examining a patient with toothache">
      <div class="abs" style="inset:0;background:linear-gradient(180deg,#b9b5b3 0%,#8f8a8c 35%,#4c4a52 62%,#1d1c22 100%)"></div>
      <div class="title" style="top:62px">Emergency Services</div>
      <div class="desc" style="top:72.5px">Urgent care when you need it most.</div>
    </article>
    <article class="card" style="left:144.6px;top:151.8px" role="img" aria-label="Before and after photo of restored teeth">
      <div class="abs" style="inset:0;background:linear-gradient(180deg,#d98b8b 0%,#b3605e 30%,#e4dccd 45%,#5a3d33 70%,#1e1818 100%)"></div>
      <div class="title" style="top:62px">Restorations</div>
      <div class="desc" style="top:72.5px">Fillings, crowns, and bridges to repair your smile.</div>
    </article>
    <article class="card" style="left:246.8px;top:151.8px" role="img" aria-label="Rendering of full dentures">
      <div class="abs" style="inset:0;background:linear-gradient(180deg,#8c8690 0%,#7b6f7a 25%,#b8545f 45%,#5a3e48 70%,#1e1a1f 100%)"></div>
      <div class="title" style="top:62px">Dentures</div>
      <div class="desc" style="top:72.5px">Full or partial dentures for restored functionality.</div>
    </article>

    <a class="btn" style="left:164.7px;top:258.6px;width:54px;height:12.8px">View All Services
      <svg viewBox="0 0 24 24"><path d="M4 12h15M13 6l6 6-6 6" stroke="#28241f" stroke-width="2.4" fill="none"/></svg></a>
  </section>

  <!-- Why choose us -->
  <section class="why">
    <div class="abs" role="img" aria-label="Photo of a dentist showing a patient an x-ray on a screen" style="left:0;top:0;width:192px;height:156px;background:linear-gradient(110deg,#eef1f3 0%,#d7e2e8 35%,#9cb3c2 60%,#3f8f95 80%,#c9a58c 100%)"></div>
    <div class="abs gold" style="left:218.7px;top:31.5px;font-size:4.4px;white-space:nowrap">Maplecrest Dentistry</div>
    <div class="rule" style="left:274.4px;top:34.3px;width:14px"></div>
    <h2 class="abs serif" style="left:218.7px;top:38.5px;font-size:10.2px;white-space:nowrap">Why Choose Us</h2>
    <ul>
      <li style="top:65px"><svg viewBox="0 0 24 24"><path d="M4 12h15M13 6l6 6-6 6" stroke="#f3a93a" stroke-width="2.4" fill="none"/></svg>Modern, Comfortable Office Environment</li>
      <li style="top:77.5px"><svg viewBox="0 0 24 24"><path d="M4 12h15M13 6l6 6-6 6" stroke="#f3a93a" stroke-width="2.4" fill="none"/></svg>Friendly, Professional Dental Team</li>
      <li style="top:90px"><svg viewBox="0 0 24 24"><path d="M4 12h15M13 6l6 6-6 6" stroke="#f3a93a" stroke-width="2.4" fill="none"/></svg>Latest Technology and Equipment</li>
      <li style="top:102.5px"><svg viewBox="0 0 24 24"><path d="M4 12h15M13 6l6 6-6 6" stroke="#f3a93a" stroke-width="2.4" fill="none"/></svg>Personalized Care for Every Patient</li>
      <li style="top:115px"><svg viewBox="0 0 24 24"><path d="M4 12h15M13 6l6 6-6 6" stroke="#f3a93a" stroke-width="2.4" fill="none"/></svg>Convenient Scheduling &amp; Emergency Support</li>
    </ul>
  </section>

  <!-- Testimonials -->
  <section class="reviews">
    <h2 class="abs center serif" style="left:192px;top:23px;font-size:13.2px">What Our Client Says</h2>
    <div class="rule" style="left:152px;top:44.8px;width:20px"></div>
    <div class="rule" style="left:210.8px;top:44.8px;width:20px"></div>
    <div class="abs center gold" style="left:192px;top:42.2px;font-size:4.4px">Testimonials</div>

    <div class="slider-arrow" style="left:24px;top:102.4px;border-color:#555"><svg viewBox="0 0 24 24"><path d="M15 5l-7 7 7 7" stroke="#333" stroke-width="2" fill="none"/></svg></div>
    <div class="slider-arrow" style="left:348.5px;top:102.4px;border-color:var(--gold)"><svg viewBox="0 0 24 24"><path d="M9 5l7 7-7 7" stroke="#f3a93a" stroke-width="2" fill="none"/></svg></div>

    <article class="review" style="left:41.7px;top:59.5px">
      <div class="inner"></div>
      <div class="avatar" role="img" aria-label="Photo of a smiling female client" style="background:linear-gradient(180deg,#f4ead6 0%,#efd9a8 55%,#9fb6d8 100%)"></div>
      <div class="stars">★★★★★</div>
      <p class="text">Maplecrest Dentistry made me feel completely at ease. They're professional, gentle, and incredibly knowledgeable. Highly recommend!</p>
      <div class="who"><i></i><div><div class="name">Clara M.</div><div class="role">Real Client</div></div></div>
      <div class="quote">”</div>
    </article>
    <article class="review" style="left:195.2px;top:59.5px">
      <div class="inner"></div>
      <div class="avatar" role="img" aria-label="Photo of a smiling male client" style="background:linear-gradient(180deg,#f4ead6 0%,#efd9a8 55%,#c9d6e4 100%)"></div>
      <div class="stars">★★★★★</div>
      <p class="text">Maplecrest Dentistry made me feel completely at ease. They're professional, gentle, and incredibly knowledgeable. Highly recommend!</p>
      <div class="who"><i></i><div><div class="name">Clara M.</div><div class="role">Real Client</div></div></div>
      <div class="quote">”</div>
    </article>

    <div class="dots" style="left:192px;top:174.5px"><span style="background:#ccc"></span><span style="background:#ccc"></span><span class="on"></span><span style="background:#ccc"></span><span style="background:#ccc"></span></div>
  </section>
</main>

<!-- Appointment form and footer -->
<section class="contact">
  <div class="team-photo" role="img" aria-label="Photo of two smiling dentists in white uniforms standing in a dental clinic"></div>
  <div class="form-box">
    <div class="abs center serif" style="left:75px;top:13.5px;font-size:7.4px">Book Your Appointment</div>
    <div class="rule" style="left:37px;top:30.4px;width:20px"></div>
    <div class="rule" style="left:92px;top:30.4px;width:20px"></div>
    <div class="abs center gold" style="left:75px;top:27.6px;font-size:4.2px">Contact Us</div>
    <div class="field" style="left:17.8px;top:38.6px;width:55px;height:10.6px">First Name *</div>
    <div class="field" style="left:76.8px;top:38.6px;width:55px;height:10.6px">Last Name *</div>
    <div class="field" style="left:17.8px;top:52.9px;width:55px;height:10.6px">Email Address *</div>
    <div class="field" style="left:76.8px;top:52.9px;width:55px;height:10.6px">Phone No. *</div>
    <div class="field" style="left:17.8px;top:67.9px;width:114px;height:20.6px">Your Message *</div>
    <a class="btn" style="left:46.5px;top:96.8px;width:56px;height:13.4px">Get In Touch
      <svg viewBox="0 0 24 24"><path d="M4 12h15M13 6l6 6-6 6" stroke="#28241f" stroke-width="2.4" fill="none"/></svg></a>
  </div>

  <div class="footer-head" style="left:82.4px;top:235.5px">Quick Links</div>
  <nav class="footer-links">
    <a style="top:247.2px">Home</a>
    <a style="top:255.6px">About Us</a>
    <a style="top:264px">Services</a>
    <a style="top:272.3px">Blog</a>
    <a style="top:280.6px">Contact Us</a>
  </nav>

  <div class="brand abs center" style="left:192px;top:232px;font-size:7px">Maplecrest Dentistry</div>
  <div class="abs" style="left:141.5px;top:272px;font-size:3px;color:#aaa;white-space:nowrap">Email Address*</div>
  <svg class="abs" style="left:236px;top:272.5px;width:4.4px;height:4.4px" viewBox="0 0 24 24"><path d="M2 11L22 2l-9 20-2-9z" fill="#fff"/></svg>
  <div class="abs" style="left:141.5px;top:279.5px;width:100px;height:0.5px;background:#777"></div>
  <span class="social" style="left:159.2px"></span>
  <span class="social" style="left:175.3px"></span>
  <span class="social" style="left:192px"></span>
  <span class="social" style="left:208.2px"></span>

  <div class="footer-head" style="left:305.6px;top:235.5px">Contact Us</div>
  <div class="c-item" style="top:249.2px"><svg viewBox="0 0 24 24"><path fill="none" stroke="#f3a93a" stroke-width="2" d="M6.6 10.8a15 15 0 0 0 6.6 6.6l2.2-2.2c.3-.3.7-.4 1-.2 1.1.4 2.3.6 3.6.6.6 0 1 .4 1 1V20c0 .6-.4 1-1 1A17 17 0 0 1 3 4c0-.6.4-1 1-1h3.5c.6 0 1 .4 1 1 0 1.3.2 2.5.6 3.6.1.3 0 .7-.2 1z"/></svg><span>(555) 014-2287</span></div>
  <div class="c-item" style="top:264.2px"><svg viewBox="0 0 24 24"><rect x="3" y="5" width="18" height="14" rx="1" fill="none" stroke="#f3a93a" stroke-width="2"/><path d="M3 6l9 7 9-7" fill="none" stroke="#f3a93a" stroke-width="2"/></svg><span>hello@maplecrestsmiles.com</span></div>
  <div class="c-item" style="top:279.5px"><svg viewBox="0 0 24 24"><path d="M12 22s7-7 7-12a7 7 0 0 0-14 0c0 5 7 12 7 12z" fill="none" stroke="#f3a93a" stroke-width="2"/><circle cx="12" cy="10" r="2.5" fill="#f3a93a"/></svg><span>48 Orchard Ave, 2nd Floor, Riverton, NY</span></div>
  <div class="c-item" style="top:294.5px"><svg viewBox="0 0 24 24"><circle cx="12" cy="12" r="9" fill="none" stroke="#f3a93a" stroke-width="2"/><path d="M12 7v5l3.5 2" fill="none" stroke="#f3a93a" stroke-width="2"/></svg><span>Mon–Fri 8am–6pm<br>Sat 9am–2pm, Sun Closed</span></div>

  <div class="abs" style="left:0;top:334.4px;width:384px;height:0.5px;background:#3c3833"></div>
  <div class="abs center" style="left:192px;top:344.4px;font-size:2.9px;color:#b5aea5">Copyright © 2025 Maplecrest Dentistry &nbsp;|&nbsp; Privacy Policy &nbsp;|&nbsp; Terms &amp; Condition</div>
</section>

<div class="thanks">Thank you for watching</div>

</body>
</html>
```